BM PowerPoint Template Refresh

I'm looking to refresh our corporate presentation collateral, namely our base PowerPoint template. I need something that sparks, and gives the appearance of our contemporary firm that is hip, innovative, and modern. The project should provide for the various slide master templates with appropriately sized background images for slides in 4:3 and 16:9 formats

Target Market(s)

Investment banking prospect and clients which are typically in the high-tech industries of software, semiconductors,telecom, and telecom components

Industry/Entity Type

Investment Banking

Font styles to use
Other font styles liked:
• Goudy Old Style

Requirements
Must have
• - Must leverage current logo (red color is the standard, however portions of the logo or, color variations from our stock are possible for use), primary and secondary current colors. Non-section text is Goudy Old Style (headers and body text)
- The PPT template must have at least all of the LAYOUT options found in the Old BM Prez
- Options with and without the Brecon logo as a transparent background
- Need a final version in 16:9 and 4:3 formats
- Must be able to add footer information such as "Confidential Information", slide number, and date
Nice to have
• a few design ideas on the IP Engineering image found on slide 7 of the New BM Prez Attempt.ppt file

```html
<!DOCTYPE html>
<html lang="en">
<head>
<meta charset="utf-8">
<title>Brecon Advisors – Presentation Deck</title>
<link href="https://fonts.googleapis.com/css2?family=Roboto:wght@400;700;900&family=Sorts+Mill+Goudy&display=swap" rel="stylesheet">
<style>
:root{
  --red:#d3202f;
  --red-soft:#f6c9cd;
  --navy:#1f3a70;
  --navy-deep:#152a55;
  --ink:#333a44;
  --muted:#8a9099;
  --paper:#ffffff;
  --canvas:#eceef1;
  --line:#d9dce1;
}
*{box-sizing:border-box;margin:0;padding:0}
html,body{width:1200px;height:2336px;overflow:hidden}
body{background:var(--canvas);font-family:"Sorts Mill Goudy",Georgia,serif;color:var(--ink);position:relative}

/* header */
.hero{position:absolute;left:0;top:0;width:1200px;height:470px;
  background:linear-gradient(180deg,#f4f5f7 0%,#e4e6ea 100%)}
.hero-photo{position:absolute;left:0;top:0;width:600px;height:470px;
  background:linear-gradient(120deg,rgba(200,204,210,.55),rgba(236,238,241,.2) 70%)}

/* company name: plain text wordmark, single colour and weight */
.brand{position:absolute;font-family:"Sorts Mill Goudy",Georgia,serif;font-weight:400;color:var(--red);white-space:nowrap;line-height:1}
.brand.on-dark{color:#fff}
.hero .brand{left:120px;top:84px;font-size:40px}

.hero-title{position:absolute;left:120px;top:280px;font-family:"Roboto",Arial,sans-serif;font-weight:900;font-size:78px;line-height:.95;color:var(--red)}
.hero-title span{display:block;color:#2b2f36;font-size:56px;font-weight:700}
.hero-slide{position:absolute;left:610px;top:40px;width:560px;height:315px;box-shadow:0 8px 24px rgba(0,0,0,.18)}

/* slide grid */
.deck{position:absolute;left:20px;top:490px;width:1160px;display:grid;grid-template-columns:repeat(3,376px);gap:20px 16px}
.slide{position:relative;width:376px;height:212px;background:var(--paper);overflow:hidden;box-shadow:0 2px 6px rgba(0,0,0,.15);font-size:7px;line-height:1.35}
.deck .last-row{grid-column:1/-1;display:flex;justify-content:center;gap:16px}

.slide .brand{font-size:13px}
.photo-navy{background:linear-gradient(135deg,#3b5c9a,#1f3a70 60%,#152a55)}
.photo-grey{background:linear-gradient(135deg,#c9ccd1,#9ea3aa 60%,#b8bcc2)}
.photo-sky{background:linear-gradient(160deg,#e9ebef,#c4c8ce)}

.s-title{position:absolute;left:18px;top:15px;right:18px;font-size:12px;color:var(--navy);white-space:nowrap;overflow:hidden}
.s-rule{position:absolute;left:18px;top:34px;width:340px;height:1px;background:var(--line)}
.foot{position:absolute;left:18px;right:18px;bottom:8px;display:flex;justify-content:space-between;font-size:5.5px;color:var(--muted)}
.foot b{width:18px;height:3px;background:var(--red);display:block;margin-top:2px}
.line{height:3px;background:var(--line);margin:4px 0;border-radius:1px}
.txt{color:var(--ink);font-size:6.5px}
.white{color:#fff}
.abs{position:absolute}
.circle{border-radius:50%}
.redbg{background:var(--red)}
.navybg{background:var(--navy)}
.cover-title{font-size:19px;line-height:1.1;letter-spacing:.5px;text-transform:uppercase}
table{border-collapse:collapse;width:100%;font-size:6px}
th{background:var(--red);color:#fff;padding:4px;text-align:left;font-weight:400}
td{padding:4px;border-bottom:1px solid var(--line)}
.navy-head th{background:var(--navy)}
</style>
</head>
<body>

<header class="hero">
  <div class="hero-photo" role="img" aria-label="Faded photo of a cheering audience with raised hands"></div>
  <div class="brand">Brecon Advisors</div>
  <h1 class="hero-title">Presentation<span>Deck</span></h1>
  <div class="hero-slide slide" style="width:560px;height:315px">
    <div class="abs" style="left:0;top:0;width:560px;height:315px;background:#fff"></div>
    <div class="abs photo-navy" role="img" aria-label="Blue-toned photo of glass office towers" style="left:0;top:60px;width:560px;height:200px"></div>
    <div class="brand" style="left:0;right:0;text-align:center;top:22px;font-size:20px">Brecon Advisors</div>
    <div class="abs white cover-title" style="left:250px;top:125px;font-size:26px">Brecon Advisory<br>Overview</div>
    <div class="abs redbg" style="left:250px;top:200px;width:40px;height:3px"></div>
  </div>
</header>

<main class="deck">
  <!-- row 1 -->
  <section class="slide">
    <div class="abs photo-navy" role="img" aria-label="Blue-toned photo of office towers" style="left:0;top:40px;width:376px;height:130px"></div>
    <div class="brand" style="left:0;right:0;text-align:center;top:14px">Brecon Advisors</div>
    <div class="abs white cover-title" style="left:170px;top:80px;font-size:16px">Brecon Advisory<br>Overview</div>
    <div class="abs redbg" style="left:170px;top:122px;width:24px;height:2px"></div>
  </section>
  <section class="slide">
    <div class="abs photo-grey" role="img" aria-label="Grey photo of a glass building facade" style="left:0;top:0;width:376px;height:212px"></div>
    <div class="abs redbg" style="left:0;top:0;width:220px;height:170px"></div>
    <div class="abs navybg" style="left:0;top:170px;width:376px;height:42px"></div>
    <div class="brand on-dark" style="left:16px;top:16px">Brecon Advisors</div>
    <div class="abs white cover-title" style="left:16px;top:70px;font-size:15px">Presentation<br>Title Goes<br>Here</div>
    <div class="abs white" style="left:16px;top:185px;font-size:6px">Subtitle and date line</div>
  </section>
  <section class="slide">
    <div class="abs navybg" style="left:0;top:0;width:376px;height:212px"></div>
    <div class="abs photo-grey circle" role="img" aria-label="Grey photo of a building in a circular crop" style="left:200px;top:20px;width:220px;height:220px"></div>
    <div class="brand on-dark" style="left:16px;top:16px">Brecon Advisors</div>
    <div class="abs white cover-title" style="left:16px;top:70px;font-size:15px">Presentation<br>Title Goes<br>Here</div>
    <div class="abs redbg" style="left:16px;top:136px;width:24px;height:2px"></div>
  </section>

  <!-- row 2 -->
  <section class="slide">
    <div class="abs navybg" style="left:110px;top:0;width:266px;height:212px"></div>
    <div class="abs redbg circle" style="left:40px;top:56px;width:100px;height:100px;border:6px solid #fff"></div>
    <div class="abs white" style="left:170px;top:62px;font-size:19px;line-height:1.15">Our Team of<br>Operational<br>Dealmakers</div>
  </section>
  <section class="slide">
    <div class="s-title">IP Engineering: Adapting Your Value to a Buyer's Rationale</div><div class="s-rule"></div>
    <svg class="abs" style="left:130px;top:50px" width="200" height="130" viewBox="0 0 200 130">
      <path d="M30 70 L150 10 L170 40 Z" fill="#d3202f"/>
      <path d="M30 70 L170 40 L175 75 Z" fill="#e45a65"/>
      <path d="M30 70 L175 75 L165 110 Z" fill="#ef939a"/>
      <path d="M30 70 L165 110 L140 128 Z" fill="#f6c9cd"/>
      <circle cx="30" cy="70" r="14" fill="#1f3a70"/>
    </svg>
    <div class="abs" style="left:20px;top:60px;width:100px"><div class="txt">Buyer rationale</div><div class="line"></div><div class="line" style="width:70%"></div><div class="line"></div></div>
    <div class="foot"><span>Confidential Information</span><b></b><span>1</span></div>
  </section>
  <section class="slide">
    <div class="s-title">IP Engineering: Adapting Your Value to a Buyer's Rationale</div><div class="s-rule"></div>
    <svg class="abs" style="left:110px;top:45px" width="160" height="140" viewBox="0 0 160 140">
      <g stroke="#d3202f" stroke-width="1"><line x1="80" y1="70" x2="80" y2="20"/><line x1="80" y1="70" x2="130" y2="70"/><line x1="80" y1="70" x2="80" y2="120"/><line x1="80" y1="70" x2="30" y2="70"/></g>
      <circle cx="80" cy="70" r="24" fill="#d3202f"/>
      <circle cx="80" cy="18" r="14" fill="#e45a65"/><circle cx="134" cy="70" r="14" fill="#e45a65"/>
      <circle cx="80" cy="122" r="14" fill="#e45a65"/><circle cx="26" cy="70" r="14" fill="#e45a65"/>
    </svg>
    <div class="foot"><span>Confidential Information</span><b></b><span>2</span></div>
  </section>

  <!-- row 3 -->
  <section class="slide">
    <div class="s-title">Brecon Advisory Overview</div><div class="s-rule"></div>
    <div class="abs" style="left:18px;top:44px;width:180px">
      <div class="txt" style="color:var(--red)">Who we are</div><div class="line"></div><div class="line" style="width:80%"></div>
      <div class="txt" style="color:var(--red);margin-top:6px">What we do</div><div class="line"></div><div class="line" style="width:60%"></div>
      <div class="txt" style="color:var(--red);margin-top:6px">How we help</div><div class="line"></div><div class="line" style="width:75%"></div>
    </div>
    <div class="abs navybg white" style="left:214px;top:44px;width:144px;height:140px;padding:10px;font-size:7px">Sector focus<br>Software<br>Semiconductors<br>Telecom<br>Components</div>
    <div class="foot"><span>Confidential Information</span><b></b><span>3</span></div>
  </section>
  <section class="slide">
    <div class="s-title">IP "Audit" Potential Buyer Process</div><div class="s-rule"></div>
    <div class="abs redbg white" style="left:90px;top:60px;padding:3px 6px;font-size:7px">Value</div>
    <div class="abs redbg white" style="left:170px;top:52px;padding:3px 6px;font-size:7px">IP Audit</div>
    <div class="abs redbg white" style="left:250px;top:60px;padding:3px 6px;font-size:7px">Buyer</div>
    <svg class="abs" style="left:60px;top:80px" width="260" height="60" viewBox="0 0 260 60"><path d="M10 40 Q130 -10 250 40" stroke="#1f3a70" stroke-width="2" fill="none"/></svg>
    <div class="abs" style="left:60px;top:150px;width:260px"><div class="line"></div><div class="line" style="width:70%"></div></div>
    <div class="foot"><span>Confidential Information</span><b></b><span>4</span></div>
  </section>
  <section class="slide">
    <div class="s-title">Add Awesome Title Here</div><div class="s-rule"></div>
    <div class="abs" style="left:18px;top:46px;width:340px;display:grid;grid-template-columns:70px 1fr;gap:8px 10px">
      <div class="redbg white" style="padding:4px;font-size:6px">Point one</div><div><div class="line"></div><div class="line" style="width:60%"></div></div>
      <div class="redbg white" style="padding:4px;font-size:6px">Point two</div><div><div class="line"></div><div class="line" style="width:70%"></div></div>
      <div class="redbg white" style="padding:4px;font-size:6px">Point three</div><div><div class="line"></div><div class="line" style="width:50%"></div></div>
      <div class="redbg white" style="padding:4px;font-size:6px">Point four</div><div><div class="line"></div><div class="line" style="width:65%"></div></div>
    </div>
    <div class="foot"><span>Confidential Information</span><b></b><span>5</span></div>
  </section>

  <!-- row 4 -->
  <section class="slide">
    <div class="s-title">Add Awesome Title Here</div><div class="s-rule"></div>
    <div class="abs" style="left:18px;top:48px;width:340px;display:grid;grid-template-columns:repeat(2,1fr);gap:10px 20px">
      <div class="txt"><span style="color:var(--red)">01</span> Market insight<div class="line"></div></div>
      <div class="txt"><span style="color:var(--red)">02</span> Deal strategy<div class="line"></div></div>
      <div class="txt"><span style="color:var(--red)">03</span> Buyer outreach<div class="line"></div></div>
      <div class="txt"><span style="color:var(--red)">04</span> Negotiation<div class="line"></div></div>
      <div class="txt"><span style="color:var(--red)">05</span> Due diligence<div class="line"></div></div>
      <div class="txt"><span style="color:var(--red)">06</span> Closing<div class="line"></div></div>
    </div>
    <div class="foot"><span>Confidential Information</span><b></b><span>6</span></div>
  </section>
  <section class="slide">
    <div class="abs photo-grey" role="img" aria-label="Black and white photo of a modern building" style="left:0;top:0;width:150px;height:212px"></div>
    <div class="abs" style="left:166px;top:18px;width:190px">
      <div style="font-size:12px;color:var(--navy)">Add Awesome Title Here</div>
      <div class="line" style="margin-top:12px"></div><div class="line"></div><div class="line" style="width:80%"></div>
      <div class="line" style="margin-top:10px"></div><div class="line"></div><div class="line" style="width:60%"></div>
    </div>
    <div class="foot" style="left:166px"><span>Confidential Information</span><b></b><span>7</span></div>
  </section>
  <section class="slide">
    <div class="s-title">Add Awesome Title Here</div><div class="s-rule"></div>
    <div class="abs" style="left:40px;top:46px;display:flex;gap:18px">
      <div class="navybg" style="width:86px;height:140px;border-radius:8px;position:relative;padding:40px 8px 0"><span class="abs redbg circle" style="left:28px;top:8px;width:30px;height:30px"></span><div class="line" style="background:#5b73a3"></div><div class="line" style="background:#5b73a3;width:70%"></div></div>
      <div class="navybg" style="width:86px;height:140px;border-radius:8px;position:relative;padding:40px 8px 0"><span class="abs redbg circle" style="left:28px;top:8px;width:30px;height:30px"></span><div class="line" style="background:#5b73a3"></div><div class="line" style="background:#5b73a3;width:70%"></div></div>
      <div class="navybg" style="width:86px;height:140px;border-radius:8px;position:relative;padding:40px 8px 0"><span class="abs redbg circle" style="left:28px;top:8px;width:30px;height:30px"></span><div class="line" style="background:#5b73a3"></div><div class="line" style="background:#5b73a3;width:70%"></div></div>
    </div>
  </section>

  <!-- row 5 -->
  <section class="slide">
    <div class="s-title">Add Awesome Title Here</div><div class="s-rule"></div>
    <div class="abs" style="left:18px;top:46px;width:340px;display:grid;grid-template-columns:repeat(2,1fr);gap:8px 20px">
      <div class="txt"><span style="color:var(--red)">■</span> Strategic review of options</div>
      <div class="txt"><span style="color:var(--red)">■</span> Valuation and positioning</div>
      <div class="txt"><span style="color:var(--red)">■</span> Targeted buyer mapping</div>
      <div class="txt"><span style="color:var(--red)">■</span> Structured sale process</div>
      <div class="txt"><span style="color:var(--red)">■</span> Term sheet negotiation</div>
      <div class="txt"><span style="color:var(--red)">■</span> Closing and integration</div>
    </div>
    <div class="foot"><span>Confidential Information</span><b></b><span>8</span></div>
  </section>
  <section class="slide">
    <div class="s-title">Add Awesome Title Here</div><div class="s-rule"></div>
    <div class="abs navybg" style="left:0;top:80px;width:376px;height:60px"></div>
    <div class="abs circle" style="left:60px;top:66px;width:80px;height:80px;background:#fff;border:3px solid var(--red)"></div>
    <div class="abs circle" style="left:148px;top:66px;width:80px;height:80px;background:#fff;border:3px solid var(--red)"></div>
    <div class="abs circle" style="left:236px;top:66px;width:80px;height:80px;background:#fff;border:3px solid var(--red)"></div>
    <div class="abs" style="left:60px;top:160px;width:256px"><div class="line"></div><div class="line" style="width:70%"></div></div>
    <div class="foot"><span>Confidential Information</span><b></b><span>9</span></div>
  </section>
  <section class="slide">
    <div class="s-title">Add Awesome Title Here</div><div class="s-rule"></div>
    <div class="abs" style="left:18px;top:50px;width:150px">
      <div class="txt"><span style="color:var(--navy)">●</span> First key point</div><div class="line"></div>
      <div class="txt"><span style="color:var(--navy)">●</span> Second key point</div><div class="line"></div>
      <div class="txt"><span style="color:var(--navy)">●</span> Third key point</div><div class="line"></div>
    </div>
    <div class="abs" style="left:196px;top:50px;width:160px"><div class="line"></div><div class="line"></div><div class="line" style="width:80%"></div><div class="line"></div><div class="line" style="width:60%"></div></div>
    <div class="foot"><span>Confidential Information</span><b></b><span>10</span></div>
  </section>

  <!-- row 6 -->
  <section class="slide">
    <div class="abs circle" style="left:250px;top:-40px;width:180px;height:180px;background:var(--red-soft)"></div>
    <div class="abs" style="left:18px;top:50px;width:180px">
      <div style="font-size:12px;color:var(--red)">Headline Statement</div>
      <div class="txt" style="margin-top:6px">A short supporting sentence sits here to frame the slide message.</div>
    </div>
    <div class="foot"><span>Confidential Information</span><b></b><span>11</span></div>
  </section>
  <section class="slide">
    <div class="abs navybg" style="left:0;top:0;width:376px;height:212px"></div>
    <div class="abs" style="left:18px;top:40px;width:340px;display:grid;grid-template-columns:repeat(3,1fr);gap:12px">
      <div class="white" style="font-size:7px">Technology<div class="line" style="background:#5b73a3"></div><div class="line" style="background:#5b73a3;width:70%"></div></div>
      <div class="white" style="font-size:7px">Markets<div class="line" style="background:#5b73a3"></div><div class="line" style="background:#5b73a3;width:60%"></div></div>
      <div class="white" style="font-size:7px">Buyers<div class="line" style="background:#5b73a3"></div><div class="line" style="background:#5b73a3;width:80%"></div></div>
    </div>
    <div class="abs" style="left:0;top:120px;width:376px;height:92px;background:#fff"></div>
    <div class="abs" style="left:18px;top:136px;width:340px"><div class="line"></div><div class="line" style="width:70%"></div></div>
  </section>
  <section class="slide">
    <div class="s-title">Add Awesome Title Here</div><div class="s-rule"></div>
    <div class="abs" style="left:18px;top:46px;width:340px">
      <table><tr><th>Metric</th><th>2019</th><th>2020</th><th>2021</th></tr>
      <tr><td>Revenue</td><td>12</td><td>18</td><td>24</td></tr>
      <tr><td>Margin</td><td>8%</td><td>11%</td><td>14%</td></tr>
      <tr><td>Deals</td><td>4</td><td>6</td><td>9</td></tr></table>
    </div>
    <div class="foot"><span>Confidential Information</span><b></b><span>12</span></div>
  </section>

  <!-- row 7 -->
  <section class="slide">
    <div class="s-title">Add Awesome Title Here</div><div class="s-rule"></div>
    <div class="abs" style="left:30px;top:56px;display:flex;gap:40px">
      <div><div class="circle" style="width:44px;height:44px;border:2px solid var(--line)"></div><div class="line" style="width:44px"></div></div>
      <div><div class="circle" style="width:44px;height:44px;border:2px solid var(--line)"></div><div class="line" style="width:44px"></div></div>
      <div><div class="circle" style="width:44px;height:44px;border:2px solid var(--line)"></div><div class="line" style="width:44px"></div></div>
      <div><div class="circle" style="width:44px;height:44px;border:2px solid var(--line)"></div><div class="line" style="width:44px"></div></div>
    </div>
    <div class="abs" style="left:30px;top:140px;display:flex;gap:60px;font-size:16px;color:var(--red)"><span>150</span><span>2015</span><span>150+</span></div>
    <div class="foot"><span>Confidential Information</span><b></b><span>13</span></div>
  </section>
  <section class="slide">
    <div class="s-title">Add Awesome Title Here</div><div class="s-rule"></div>
    <div class="abs" style="left:18px;top:46px;width:340px">
      <table class="navy-head"><tr><th>Company</th><th>Sector</th><th>Value</th></tr>
      <tr><td>Client A</td><td>Software</td><td>$45M</td></tr>
      <tr><td>Client B</td><td>Telecom</td><td>$80M</td></tr>
      <tr><td>Client C</td><td>Semis</td><td>$62M</td></tr></table>
    </div>
    <div class="foot"><span>Confidential Information</span><b></b><span>14</span></div>
  </section>
  <section class="slide">
    <div class="s-title">Add Awesome Title Here</div><div class="s-rule"></div>
    <svg class="abs" style="left:128px;top:46px" width="120" height="130" viewBox="0 0 120 130">
      <rect x="45" y="0" width="30" height="50" fill="#1f3a70"/><rect x="45" y="80" width="30" height="50" fill="#d3202f"/>
      <rect x="0" y="50" width="45" height="30" fill="#d3202f"/><rect x="75" y="50" width="45" height="30" fill="#1f3a70"/>
      <circle cx="60" cy="65" r="14" fill="#fff" stroke="#d3202f" stroke-width="3"/>
    </svg>
    <div class="foot"><span>Confidential Information</span><b></b><span>15</span></div>
  </section>

  <!-- row 8 -->
  <div class="last-row">
    <section class="slide">
      <div class="brand" style="left:110px;top:78px;font-size:18px">Brecon Advisors</div>
      <div class="abs txt" style="left:110px;top:120px;color:var(--muted)">100 Harbor Way, Suite 2<br>contact@breconadvisors.example</div>
    </section>
    <section class="slide">
      <div class="abs photo-sky" role="img" aria-label="Light grey photo of a skyscraper" style="left:0;top:0;width:376px;height:212px"></div>
      <div class="abs redbg" style="left:0;top:150px;width:376px;height:62px;opacity:.9"></div>
      <div class="abs white" style="left:18px;top:168px;font-size:12px">Thank You</div>
    </section>
  </div>
</main>

</body>
</html>
```